" A empresa é afiliada a Vantrel Investimentos e atua com produtos financeiros de investimentos: Fundos, Aplicaçoes de Renda Fixa, Açoes, Mercado Futuro e Derivativos. "

```html
<!DOCTYPE html>
<html lang="pt-BR">
<head>
<meta charset="utf-8">
<title>Pasta de documentos – Axiomar</title>
<link href="https://fonts.googleapis.com/css2?family=Questrial&display=swap" rel="stylesheet">
<style>
  :root{
    --backdrop:#d9d9db;
    --paper:#ffffff;
    --paper-shade:#f1f1f3;
    --fold:#c9c9cd;
    --edge:#b5b5ba;
    --ink-blue:#2f5f8a;
    --ink-grey:#6d6e72;
    --ink-dark:#3c3d40;
    --mark-dark:#2b2b2d;
  }
  html,body{margin:0;padding:0;overflow:hidden}
  body{width:1200px;height:1200px;background:var(--backdrop);font-family:"Questrial",sans-serif;position:relative}
  .folder-dieline{position:absolute;left:0;top:0;width:1200px;height:1200px}
  .brand-block{position:absolute;left:650px;top:282px;display:flex;align-items:center;gap:12px}
  .brand-dot{width:36px;height:36px;border-radius:50%;background:var(--ink-blue)}
  .brand-name{font-size:31px;letter-spacing:3px;color:var(--ink-blue);line-height:1}
  .brand-tag{font-size:8.5px;letter-spacing:1.4px;color:var(--ink-grey);margin-top:4px}
  .partner-block{position:absolute;left:650px;top:352px;display:flex;gap:12px;align-items:center}
  .partner-square{width:58px;height:58px;background:var(--mark-dark)}
  .partner-lead{font-size:14px;color:var(--ink-grey)}
  .partner-name{font-size:30px;color:var(--ink-grey);line-height:1.1}
  .partner-note{font-size:7px;color:var(--ink-grey);text-align:right;margin-top:2px}
  .contact-block{position:absolute;left:258px;top:603px;color:var(--ink-dark);font-size:9.5px;line-height:1.45}
  .contact-name{font-size:16px;letter-spacing:2px;color:var(--ink-blue);line-height:1}
  .contact-tag{font-size:10px;letter-spacing:.6px;color:var(--ink-grey);margin-bottom:14px}
  .contact-gap{height:12px}
</style>
</head>
<body>
<svg class="folder-dieline" viewBox="0 0 1200 1200" aria-hidden="true">
  <defs>
    <linearGradient id="paperShade" x1="0" y1="0" x2="0" y2="1">
      <stop offset="0" stop-color="var(--paper)"/>
      <stop offset="1" stop-color="var(--paper-shade)"/>
    </linearGradient>
  </defs>
  <!-- top glue strip -->
  <path d="M238 245 L1002 245 L1008 259 L230 259 Z" fill="var(--paper)" stroke="var(--edge)" stroke-width="1"/>
  <!-- cover panels -->
  <rect x="230" y="259" width="778" height="533" fill="url(#paperShade)" stroke="var(--edge)" stroke-width="1"/>
  <line x1="624" y1="259" x2="624" y2="792" stroke="var(--fold)" stroke-width="1.5"/>
  <!-- inner pocket -->
  <path d="M230 792 L134 763 L96 768 L115 960 L144 984 L612 984 L612 804
           C528 792 480 828 432 888 C396 931 360 948 312 943 L264 943 L240 816 Z"
        fill="var(--paper)" stroke="var(--edge)" stroke-width="1"/>
  <line x1="144" y1="984" x2="134" y2="763" stroke="var(--fold)" stroke-width="1"/>
  <line x1="260" y1="830" x2="272" y2="848" stroke="var(--fold)" stroke-width="1.5"/>
  <line x1="292" y1="910" x2="304" y2="928" stroke="var(--fold)" stroke-width="1.5"/>
</svg>

<div class="brand-block">
  <div class="brand-dot"></div>
  <div>
    <div class="brand-name">AXIOMAR</div>
    <div class="brand-tag">AGENTES AUTÔNOMOS DE INVESTIMENTOS</div>
  </div>
</div>

<div class="partner-block">
  <div class="partner-square"></div>
  <div>
    <div class="partner-lead">Um agente de investimento da</div>
    <div class="partner-name">Vantrel Investimentos</div>
    <div class="partner-note">Ouvidoria: 0800 000 0000</div>
  </div>
</div>

<div class="contact-block">
  <div class="contact-name">AXIOMAR</div>
  <div class="contact-tag">Agentes Autônomos De Investimentos</div>
  <div>Rua das Acácias, 215 Cj. 38</div>
  <div>Vila Serena · São Paulo SP · CEP: 04512-000</div>
  <div class="contact-gap"></div>
  <div>(11) 4000-1234</div>
  <div>contato@axiomarinvest.com.br</div>
  <div>www.axiomarinvestimentos.com.br</div>
</div>
</body>
</html>
```